Business Card and Letterhead Design for Public Accounting Firm

Business card and letterhead design for a CPA Firm located in Orange County, CA. We're looking for a modern and professional design utilizing our existing logo. We'd like a clean "less is more" look, but also something that catches the eye. We provide a high level of service to our clients. Open to single or double sided business cards.

Additional info: color numbers on logo
Blue :
R 0
G 83
B 125

#00537D

Silver :

R 154
G 154
B 154

#9A9A9A

Target Market(s)

Businesses and individuals

Industry/Entity Type

Accounting

Contact Information for Business Card

Moss Whitfield & Danby LLP - 4827 Larkspur Vale Road, Irvine, CA 92614 - (949)731-2864 - mwdaccts.example

Font styles to use
Serif
Sans Serif
Other font styles liked:
• See font file uploaded

Colors
0054AA
0677BA
7BADD7
CADEEF
E8F1F8

Requirements
Nice to have
• Possibly use the font file provided which matches our logo, but adjust to be not in all caps

```html
<!DOCTYPE html>
<html lang="en">
<head>
<meta charset="utf-8">
<title>Moss Whitfield &amp; Danby LLP — Stationery</title>
<link rel="stylesheet" href="https://fonts.googleapis.com/css2?family=Cinzel:wght@500&family=Crimson+Pro:wght@400;600&family=Lato:wght@400&display=swap">
<style>
  :root {
    --brand-blue: #00537d;
    --brand-silver: #9a9a9a;
    --backdrop: #d9d9d9;
    --paper: #ffffff;
    --ink: #333333;
    --watermark: #e6eef3;
  }
  * { margin: 0; padding: 0; box-sizing: border-box; }
  html, body { width: 1200px; height: 903px; overflow: hidden; }
  body { background: var(--backdrop); position: relative; font-family: "Crimson Pro", Georgia, serif; color: var(--ink); }

  .brand-lockup { position: absolute; display: flex; align-items: center; gap: 12px; }
  .brand-lockup__mark { background: var(--brand-blue); flex: none; }
  .brand-lockup__name { font-family: "Cinzel", Georgia, serif; font-weight: 500; line-height: 1.1; letter-spacing: 0.08em; text-transform: uppercase; }
  .brand-lockup--primary { left: 161px; top: 165px; }
  .brand-lockup--primary .brand-lockup__mark { width: 46px; height: 46px; }
  .brand-lockup--primary .brand-lockup__name { font-size: 21px; color: var(--brand-blue); }
  .brand-lockup--silver .brand-lockup__name { color: var(--brand-silver); }

  .card { position: absolute; left: 122px; width: 392px; height: 223px; background: var(--paper); border-radius: 13px; overflow: hidden; box-shadow: 0 1px 2px rgba(0,0,0,0.15); }
  .card--front { top: 276px; }
  .card--back { top: 569px; border-radius: 22px; }

  .card__header { height: 62px; background: var(--brand-blue); color: #fff; text-align: center; padding-top: 17px; }
  .card__person { font-family: "Crimson Pro", Georgia, serif; font-weight: 600; font-size: 14px; letter-spacing: 0.06em; text-transform: uppercase; line-height: 1; transform: translateX(-14px); }
  .card__role { font-size: 8.5px; margin-top: 3px; transform: translateX(-14px); }

  .card__firm-name { position: absolute; left: 60px; top: 124px; width: 122px; font-family: "Cinzel", Georgia, serif; font-weight: 500; font-size: 13px; line-height: 1.2; letter-spacing: 0.04em; color: var(--brand-blue); text-align: center; }
  .card__rule { position: absolute; left: 192px; top: 100px; width: 1px; height: 76px; background: var(--brand-blue); }
  .card__details { position: absolute; left: 206px; top: 96px; font-size: 9.5px; line-height: 12.7px; }
  .card__details .firm { color: var(--brand-blue); }
  .card__details .contact { margin-top: 6px; }
  .contact-line { display: flex; align-items: center; gap: 4px; }
  .contact-line svg { width: 7px; height: 7px; fill: var(--brand-blue); flex: none; }

  .card--back .brand-lockup { left: 74px; top: 90px; }
  .card--back .brand-lockup__mark { width: 38px; height: 38px; }
  .card--back .brand-lockup__name { font-size: 18px; }

  .view-label { position: absolute; font-family: "Lato", Arial, sans-serif; font-size: 13.5px; letter-spacing: 0.12em; color: #222; transform: translateX(-50%); }

  .letter { position: absolute; left: 578px; top: 91px; width: 497px; height: 701px; background: var(--paper); box-shadow: 0 1px 2px rgba(0,0,0,0.12); overflow: hidden; }
  .letter .brand-lockup { left: 50%; top: 32px; transform: translateX(-50%); }
  .letter .brand-lockup__mark { width: 34px; height: 34px; }
  .letter .brand-lockup__name { font-size: 14px; white-space: nowrap; }
  .letter__watermark { position: absolute; left: 0; right: 0; top: 280px; text-align: center; font-family: "Cinzel", Georgia, serif; font-weight: 500; font-size: 54px; line-height: 1.05; letter-spacing: 0.04em; color: var(--watermark); text-transform: uppercase; }
  .letter__footer { position: absolute; left: 0; bottom: 0; width: 100%; height: 57px; background: var(--brand-blue); color: #fff; font-size: 10.5px; line-height: 13.5px; text-align: center; padding-top: 15px; }
  .letter__footer .contact-line { justify-content: center; gap: 3px; }
  .letter__footer svg { width: 7px; height: 7px; fill: #fff; }
  .letter__footer .sep { width: 4px; }
</style>
</head>
<body>

  <div class="brand-lockup brand-lockup--primary">
    <span class="brand-lockup__mark"></span>
    <span class="brand-lockup__name">Moss Whitfield<br>&amp; Danby LLP</span>
  </div>

  <section class="card card--front" aria-label="Business card front">
    <header class="card__header">
      <p class="card__person">Daniel Hargrove</p>
      <p class="card__role">Founder &amp; CEO</p>
    </header>
    <p class="card__firm-name">Moss Whitfield &amp; Danby</p>
    <span class="card__rule"></span>
    <div class="card__details">
      <p class="firm">Moss Whitfield &amp; Danby LLP</p>
      <p>4827 Larkspur Vale Road</p>
      <p>Irvine, CA 92614</p>
      <div class="contact">
        <p class="contact-line"><svg viewBox="0 0 10 10"><path d="M2 0.5 L4 2.8 L3 4 Q4.5 6 6 7 L7.2 6 L9.5 8 L8 9.6 Q3 9 0.4 2 Z"/></svg>(949)731-2864</p>
        <p class="contact-line"><svg viewBox="0 0 10 10"><path d="M0.5 2 H9.5 V8 H0.5 Z M0.5 2 L5 5.5 L9.5 2" stroke="#fff" stroke-width="0.6"/></svg>cpas@mwdaccts.example</p>
        <p class="contact-line"><svg viewBox="0 0 10 10"><circle cx="5" cy="5" r="4.5"/><path d="M5 0.5 V9.5 M0.5 5 H9.5" stroke="#fff" stroke-width="0.8"/></svg>mwdaccts.example</p>
      </div>
    </div>
  </section>
  <p class="view-label" style="left:318px; top:523px;">FRONT</p>

  <section class="card card--back" aria-label="Business card back">
    <div class="brand-lockup brand-lockup--silver">
      <span class="brand-lockup__mark"></span>
      <span class="brand-lockup__name">Moss Whitfield<br>&amp; Danby LLP</span>
    </div>
  </section>
  <p class="view-label" style="left:318px; top:816px;">BACK</p>

  <section class="letter" aria-label="Letterhead">
    <div class="brand-lockup brand-lockup--silver">
      <span class="brand-lockup__mark"></span>
      <span class="brand-lockup__name">Moss Whitfield<br>&amp; Danby LLP</span>
    </div>
    <p class="letter__watermark">Moss Whitfield<br>&amp; Danby</p>
    <footer class="letter__footer">
      <p class="contact-line"><svg viewBox="0 0 10 10"><path d="M5 0.3 A3.3 3.3 0 0 1 8.3 3.6 Q8.3 5.6 5 9.7 Q1.7 5.6 1.7 3.6 A3.3 3.3 0 0 1 5 0.3 Z"/></svg>4827 Larkspur Vale Road, Irvine, CA 92614</p>
      <p class="contact-line">
        <svg viewBox="0 0 10 10"><path d="M2 0.5 L4 2.8 L3 4 Q4.5 6 6 7 L7.2 6 L9.5 8 L8 9.6 Q3 9 0.4 2 Z"/></svg>(949)731-2864<span class="sep"></span>
        <svg viewBox="0 0 10 10"><path d="M0.5 2 H9.5 V8 H0.5 Z"/></svg>cpas@mwdaccts.example<span class="sep"></span>
        <svg viewBox="0 0 10 10"><circle cx="5" cy="5" r="4.5"/></svg>mwdaccts.example
      </p>
    </footer>
  </section>
  <p class="view-label" style="left:826px; top:816px;">LETTER</p>

</body>
</html>
```